Need a business card for our overland brand!

We had the logo made and we need a great design for our business card. Use the logo provide or tweak it however you see fit.

Contact Information for Business Card

Name, Title, Telephone, email, website

```html
<!DOCTYPE html>
<html lang="en">
<head>
<meta charset="utf-8">
<title>Icefield Rovers – Business Card</title>
<link href="https://fonts.googleapis.com/css2?family=Open+Sans:wght@300;400;600;700&display=swap" rel="stylesheet">
<style>
  :root {
    --backdrop: #c0bfbd;
    --card-light: #fbfbfc;
    --card-mid: #eff0f2;
    --card-shade: #d9dbdf;
    --navy: #24364f;
    --ink: #1f3e5a;
    --slate: #5f6e7b;
    --teal: #1fa3c4;
    --black: #1b1b1b;
  }
  * { margin: 0; padding: 0; box-sizing: border-box; }
  html, body {
    width: 1200px; height: 1200px; overflow: hidden;
    background: var(--backdrop);
    font-family: "Open Sans", Arial, sans-serif;
  }
  .canvas { position: relative; width: 1200px; height: 1200px; }

  .card {
    position: absolute; left: 330px; width: 577px; height: 329px;
    background:
      linear-gradient(45deg, var(--card-shade) 0%, var(--card-mid) 30%, var(--card-light) 60%, var(--card-mid) 100%);
    overflow: hidden;
  }
  .card--front { top: 237px; }
  .card--back { top: 614px; }

  .brand-name {
    position: absolute;
    font-weight: 700;
    color: var(--navy);
    text-transform: uppercase;
    letter-spacing: -0.5px;
    line-height: 1.02;
    text-align: center;
  }
  .card--front .brand-name {
    left: 0; right: 0; top: 110px; font-size: 46px;
  }
  .card--back .brand-name {
    left: 0; width: 291px; top: 118px; font-size: 38px;
  }

  .divider {
    position: absolute; left: 290px; top: 76px; width: 2px; height: 204px;
    background: linear-gradient(to bottom, rgba(0,0,0,0), rgba(0,0,0,0.08) 50%, rgba(0,0,0,0));
  }

  .holder { position: absolute; left: 321px; top: 26px; }
  .holder__name {
    font-size: 25px; font-weight: 300; color: var(--slate);
    letter-spacing: 0.5px; line-height: 1.1; white-space: nowrap;
  }
  .holder__name strong { font-weight: 700; }
  .holder__title { font-size: 17px; font-weight: 400; color: var(--black); margin-top: 2px; }

  .contact { position: absolute; left: 333px; width: 240px; list-style: none; }
  .contact__item {
    position: absolute; left: 0; display: flex; align-items: center; gap: 8px;
    height: 32px;
  }
  .contact__icon { width: 32px; height: 32px; flex: none; }
  .contact__text {
    font-size: 9.5px; font-weight: 600; color: var(--ink);
    text-transform: uppercase; line-height: 1.4; white-space: nowrap;
  }
</style>
</head>
<body>
<div class="canvas">

  <section class="card card--front" aria-label="Card front">
    <p class="brand-name">Icefield<br>Rovers</p>
  </section>

  <section class="card card--back" aria-label="Card back">
    <p class="brand-name">Icefield<br>Rovers</p>
    <div class="divider"></div>

    <div class="holder">
      <p class="holder__name">MARCUS <strong>HALE</strong></p>
      <p class="holder__title">Managing Director</p>
    </div>

    <ul class="contact">
      <li class="contact__item" style="top:87px">
        <svg class="contact__icon" viewBox="0 0 32 32" aria-hidden="true">
          <circle cx="16" cy="16" r="16" fill="var(--teal)"/>
          <rect x="8" y="10.5" width="16" height="11" fill="none" stroke="#fff" stroke-width="1.6"/>
          <path d="M8 10.5 L16 17 L24 10.5 M8 21.5 L13.5 16 M24 21.5 L18.5 16" fill="none" stroke="#fff" stroke-width="1.4"/>
        </svg>
        <span class="contact__text">info@icefieldrovers.com</span>
      </li>
      <li class="contact__item" style="top:136px">
        <svg class="contact__icon" viewBox="0 0 32 32" aria-hidden="true">
          <circle cx="16" cy="16" r="16" fill="var(--teal)"/>
          <path d="M11 8.5c1-.6 2-.3 2.5.6l1.5 2.8c.4.8.1 1.6-.6 2l-1.1.7c.7 2 2 3.6 3.9 4.8l.9-.9c.6-.6 1.5-.6 2.1 0l2.2 2c.7.7.7 1.7 0 2.4l-1 1c-1.3 1.2-3.6.8-6-1-2.6-2-4.6-4.8-5.4-7.6-.6-2.4-.2-4.2 1-5.1z" fill="#fff"/>
        </svg>
        <span class="contact__text">+1 555 0142 7789<br>+1 555 0198 7684</span>
      </li>
      <li class="contact__item" style="top:190px">
        <svg class="contact__icon" viewBox="0 0 32 32" aria-hidden="true">
          <circle cx="16" cy="16" r="16" fill="var(--teal)"/>
          <path d="M7 16 L16 8 L25 16" fill="none" stroke="#fff" stroke-width="2.2" stroke-linejoin="round"/>
          <path d="M10 15.5 V24 H14.5 V19 H17.5 V24 H22 V15.5 L16 10.5 Z" fill="#fff"/>
        </svg>
        <span class="contact__text">48 Alder Ridge Road<br>North Pass, AK, USA</span>
      </li>
      <li class="contact__item" style="top:239px">
        <svg class="contact__icon" viewBox="0 0 32 32" aria-hidden="true">
          <circle cx="16" cy="16" r="16" fill="var(--teal)"/>
          <circle cx="16" cy="16" r="8" fill="none" stroke="#fff" stroke-width="1.6"/>
          <ellipse cx="16" cy="16" rx="3.5" ry="8" fill="none" stroke="#fff" stroke-width="1.2"/>
          <path d="M8 16 H24 M9.5 12 H22.5 M9.5 20 H22.5" stroke="#fff" stroke-width="1.1"/>
        </svg>
        <span class="contact__text">www.icefieldrovers.com</span>
      </li>
    </ul>
  </section>

</div>
</body>
</html>
```